Need a design for Office wall, Pull up banner and brochure.

Hi there, We are looking for a design for our Mission, Vision and Values. We need it for our wall design, our pull up banner, and for our brochure. Full instructions have been provided in the Instructions png file submitted. Please let me know.

Our brand colours are:

Brand colours:
#0070BA
#000A3F
#6D6E71

Font styles to use
Other font styles liked:
• FF Meta Georgian Book

Colors

Designer to choose colors to be used in the design.

```html
<!DOCTYPE html>
<html lang="en">
<head>
<meta charset="utf-8">
<title>Our Vision, Mission and Value</title>
<link rel="stylesheet" href="https://fonts.googleapis.com/css2?family=Arimo:wght@700&display=swap">
<style>
  :root {
    --bg-center: #ffffff;
    --bg-edge: #e3e3e3;
    --hub-top: #0008ea;
    --hub-bottom: #0000b8;
    --hub-shade: #000058;
    --vision-top: #00ccff;
    --vision-main: #3390f5;
    --mission-top: #ff6600;
    --mission-main: #d05a3c;
    --value-top: #0bc40b;
    --value-main: #138c13;
    --core: #ffffff;
    --icon: #000000;
  }
  html, body {
    margin: 0;
    padding: 0;
    width: 1200px;
    height: 840px;
    overflow: hidden;
  }
  body {
    background: radial-gradient(ellipse at 50% 55%, var(--bg-center) 0%, #f1f1f1 55%, var(--bg-edge) 100%);
  }
  .poster {
    position: relative;
    width: 1200px;
    height: 840px;
  }
  .poster__graphic {
    position: absolute;
    inset: 0;
  }
  .pillar-label {
    position: absolute;
    margin: 0;
    width: 300px;
    transform: translateX(-50%);
    text-align: center;
    font-family: "Arimo", Arial, sans-serif;
    font-weight: 700;
    font-size: 27px;
    line-height: 1;
    letter-spacing: 0.2px;
    white-space: pre;
  }
  .pillar-label--vision { left: 265px; top: 510px; color: var(--vision-main); }
  .pillar-label--mission { left: 600px; top: 686px; color: var(--mission-main); }
  .pillar-label--value { left: 935px; top: 510px; color: var(--value-main); }
</style>
</head>
<body>
<main class="poster">
  <svg class="poster__graphic" width="1200" height="840" viewBox="0 0 1200 840" aria-hidden="true">
    <defs>
      <linearGradient id="hub-fill" x1="0" y1="0" x2="0" y2="1">
        <stop offset="0" stop-color="var(--hub-top)"/>
        <stop offset="1" stop-color="var(--hub-bottom)"/>
      </linearGradient>
      <linearGradient id="ring-vision" x1="0" y1="0" x2="0" y2="1">
        <stop offset="0" stop-color="var(--vision-top)"/>
        <stop offset="0.55" stop-color="var(--vision-main)"/>
      </linearGradient>
      <linearGradient id="ring-mission" x1="0" y1="0" x2="0" y2="1">
        <stop offset="0" stop-color="var(--mission-top)"/>
        <stop offset="0.5" stop-color="var(--mission-main)"/>
      </linearGradient>
      <linearGradient id="ring-value" x1="0" y1="0" x2="0" y2="1">
        <stop offset="0" stop-color="var(--value-top)"/>
        <stop offset="0.45" stop-color="var(--value-main)"/>
      </linearGradient>
      <filter id="soft-blur" x="-30%" y="-30%" width="160%" height="160%">
        <feGaussianBlur stdDeviation="6"/>
      </filter>
      <filter id="hub-drop" x="-20%" y="-20%" width="140%" height="140%">
        <feDropShadow dx="0" dy="4" stdDeviation="4" flood-color="#000" flood-opacity="0.18"/>
      </filter>
      <clipPath id="clip-vision"><circle cx="265" cy="296" r="168"/></clipPath>
      <clipPath id="clip-mission"><circle cx="600" cy="464" r="168"/></clipPath>
      <clipPath id="clip-value"><circle cx="935" cy="296" r="168"/></clipPath>
      <mask id="pupil-mask">
        <rect x="-60" y="-60" width="120" height="120" fill="#fff"/>
        <circle cx="19" cy="-27" r="21" fill="#000"/>
      </mask>
    </defs>

    <!-- Connected hub shape -->
    <g class="hub" filter="url(#hub-drop)" fill="url(#hub-fill)">
      <line x1="265" y1="296" x2="600" y2="464" stroke="var(--hub-top)" stroke-width="66"/>
      <line x1="935" y1="296" x2="600" y2="464" stroke="var(--hub-top)" stroke-width="66"/>
      <circle cx="265" cy="296" r="168"/>
      <circle cx="600" cy="464" r="168"/>
      <circle cx="935" cy="296" r="168"/>
    </g>

    <!-- Inner shading -->
    <g class="hub-shade" fill="var(--hub-shade)" filter="url(#soft-blur)">
      <circle cx="265" cy="310" r="130" clip-path="url(#clip-vision)"/>
      <circle cx="600" cy="478" r="130" clip-path="url(#clip-mission)"/>
      <circle cx="935" cy="310" r="130" clip-path="url(#clip-value)"/>
    </g>

    <!-- Vision -->
    <g class="pillar pillar--vision" transform="translate(265 296)">
      <circle r="128" fill="url(#ring-vision)"/>
      <circle r="98" fill="var(--core)"/>
      <g class="icon icon--eye">
        <circle r="47" fill="none" stroke="var(--icon)" stroke-width="8"/>
        <circle cx="-1" cy="1" r="32" fill="var(--icon)" mask="url(#pupil-mask)"/>
      </g>
    </g>

    <!-- Mission -->
    <g class="pillar pillar--mission" transform="translate(600 464)">
      <circle r="128" fill="url(#ring-mission)"/>
      <circle r="98" fill="var(--core)"/>
      <g class="icon icon--target">
        <circle r="47" fill="none" stroke="var(--icon)" stroke-width="8"/>
        <circle r="24" fill="none" stroke="var(--icon)" stroke-width="8"/>
        <line x1="2" y1="-2" x2="44" y2="-44" stroke="var(--core)" stroke-width="14"/>
        <line x1="2" y1="-2" x2="38" y2="-38" stroke="var(--icon)" stroke-width="5" stroke-linecap="round"/>
        <path d="M29 -29 L27 -35 L41 -49 L44 -41 L52 -38 L38 -24 L32 -26 Z" fill="var(--icon)" stroke="var(--icon)" stroke-width="2" stroke-linejoin="round"/>
      </g>
    </g>

    <!-- Value -->
    <g class="pillar pillar--value" transform="translate(935 296)">
      <circle r="128" fill="url(#ring-value)"/>
      <circle r="98" fill="var(--core)"/>
      <g class="icon icon--star" transform="translate(0 2)">
        <polygon points="0,-46 14.7,-20.2 43.7,-14.2 23.8,7.7 27,37.2 0,25 -27,37.2 -23.8,7.7 -43.7,-14.2 -14.7,-20.2"
                 fill="none" stroke="var(--icon)" stroke-width="7" stroke-linejoin="round"/>
        <polygon points="0,-18 4.7,-6.5 17.1,-5.6 7.6,2.5 10.6,14.6 0,8 -10.6,14.6 -7.6,2.5 -17.1,-5.6 -4.7,-6.5"
                 fill="var(--icon)" stroke="var(--icon)" stroke-width="2" stroke-linejoin="round"/>
      </g>
    </g>
  </svg>

  <h2 class="pillar-label pillar-label--vision">OUR  VISION</h2>
  <h2 class="pillar-label pillar-label--mission">OUR MISSION</h2>
  <h2 class="pillar-label pillar-label--value">OUR VALUE</h2>
</main>
</body>
</html>
```